Startup Technology Consulting Firm in NYC Needs A Website

I need a website built for my startup technology consulting company Brightmoor Systems Collective. We offer a unique white glove service that provides end to end technology support. I want to stand out above the rest. We are small firm but are very dedicated which where we derive our name from BSC primarily offers
end to end technology advisory services to small businesses lacking their own IT staff. We offer top notch white glove and our customer service and satisfaction is exceed by no one.

Below are some of what we provide our clients

Strategic IT Planning
Business Continuity Planning/Disaster Recovery
Cloud Computing\DataCenter Solutions
Server Infrastructure/Networking
Virtualization Technologies
Project Management

Our Technology Advisors hold many certifications from Quillora & Tessfold. We are also Quillora Partners

I have attached my logo (preview design) As soon as I ge the final images I will upload.

Reason: want to give more time to submit designs

Industry/Entity Type

Information Technology

Coding

Coded - Design and coding required

Number of Pages Required

1 page

Font styles to use
Sans Serif

Requirements
Must have
• Attract Target Market. The site should bleed the company vision
• DEDICATION everything about the site should show this
• Layout the Benefits of our offerings
• Links to my social media
• Links to dircct my client's for remote support

```html
<!DOCTYPE html>
<html lang="en">
<head>
<meta charset="utf-8">
<title>Brightmoor Systems Collective</title>
<link href="https://fonts.googleapis.com/css2?family=Lato:wght@400;700;900&family=Montserrat:wght@600;700;800&display=swap" rel="stylesheet">
<style>
:root{
  --indigo:#3a33a3;
  --indigo-deep:#2c2787;
  --indigo-band:rgba(58,51,163,.88);
  --sky:#3aa0e6;
  --tile:#1c7fd0;
  --ink:#333;
  --muted:#666;
  --paper:#fff;
  --mist:#f0f0f2;
  --night:#05060f;
}
*{box-sizing:border-box;margin:0;padding:0}
html,body{width:1200px;height:2791px;overflow:hidden}
body{font-family:"Lato",Arial,sans-serif;color:var(--ink);background:var(--paper);position:relative}
.heading{font-family:"Montserrat",Arial,sans-serif;font-weight:800;color:var(--indigo);text-transform:uppercase}
.btn{display:inline-block;background:var(--indigo);color:#fff;font-family:"Montserrat",Arial,sans-serif;font-weight:700;font-size:16px;text-transform:uppercase;padding:11px 16px;border-radius:3px;text-decoration:none}

/* top bar */
.topbar{position:absolute;top:0;left:0;width:1200px;height:42px;background:var(--indigo);color:#fff;font-size:14px;display:flex;justify-content:flex-end;align-items:center;gap:34px;padding-right:30px;z-index:3}
.topbar span{display:flex;align-items:center;gap:8px}
.social{display:flex;gap:8px}
.social i{width:16px;height:16px;border-radius:3px;background:#fff;display:block}
.brand{position:absolute;top:0;left:20px;width:240px;height:144px;background:#fff;z-index:4;display:flex;flex-direction:column;align-items:center;justify-content:center;gap:10px}
.brand .dot{width:44px;height:44px;border-radius:50%;background:#b8c6dd}
.brand .name{font-family:"Lato",sans-serif;font-weight:700;color:var(--indigo);font-size:17px;text-align:center;line-height:1.2}

/* hero */
.hero{position:absolute;top:42px;left:0;width:1200px;height:790px}
.hero-photo{position:absolute;inset:0;background:radial-gradient(circle at 60% 50%,#3f7bff 0,#1a2bb0 12%,#0a0f40 35%,var(--night) 65%)}
.nav{position:absolute;top:56px;right:26px;display:flex;gap:8px;font-family:"Montserrat",sans-serif;font-weight:700;font-size:15px;color:#fff;text-transform:uppercase}
.nav a{color:#fff;text-decoration:none;padding:7px 8px;border-radius:3px}
.nav a.active{background:var(--indigo)}
.hero-band{position:absolute;left:0;bottom:0;width:1200px;height:189px;background:var(--indigo-band);color:#fff;font-size:25px;line-height:1.3;text-align:center;padding:36px 90px 0}

.divider{position:absolute;left:570px;width:60px;height:60px;border-radius:50%;background:#fff;border:4px solid #dfe6f2;z-index:5}

/* about */
.about{position:absolute;top:832px;left:0;width:1200px;height:378px;background:#fff}
.about h2{position:absolute;left:83px;top:50px;font-size:31px}
.about .copy{position:absolute;left:83px;top:104px;width:590px;font-size:14.5px;line-height:1.45;color:var(--muted)}
.about .copy p{margin-bottom:16px}
.about .btn{position:absolute;left:83px;top:298px}
.video{position:absolute;left:732px;top:100px;width:390px;height:205px;background:linear-gradient(135deg,#0c3f8d,#2f8ee0 55%,#9fd3f5);box-shadow:0 6px 14px rgba(0,0,0,.3);border:6px solid #fff}
.video .play{position:absolute;left:155px;top:60px;width:80px;height:80px;border-radius:50%;background:rgba(255,255,255,.85)}
.video .play:after{content:"";position:absolute;left:32px;top:24px;border-left:24px solid var(--tile);border-top:16px solid transparent;border-bottom:16px solid transparent}

/* services */
.services{position:absolute;top:1210px;left:0;width:1200px;height:402px;background:linear-gradient(180deg,#3b34a8,#342e98)}
.services h2{position:absolute;top:42px;width:100%;text-align:center;color:#fff;font-size:30px}
.service{position:absolute;width:340px;display:flex;gap:12px}
.service .tile{flex:0 0 94px;height:94px;background:var(--tile);border:3px solid #fff;display:flex;align-items:center;justify-content:center}
.service h3{font-size:17px;color:var(--sky);font-weight:700;line-height:1.2;margin-bottom:3px}
.service p{font-size:14px;line-height:1.2;color:#fff}

/* benefits */
.benefits{position:absolute;top:1612px;left:0;width:1200px;height:434px;background:#fff}
.benefits h2{position:absolute;top:46px;width:100%;text-align:center;font-size:29px}
.benefit{position:absolute;top:116px;width:300px;text-align:center}
.benefit .frame{width:114px;height:114px;margin:0 auto;border:3px solid var(--indigo);border-radius:4px;display:flex;align-items:center;justify-content:center}
.benefit h3{font-family:"Montserrat",sans-serif;font-weight:700;color:var(--indigo);font-size:19px;margin-top:24px}
.benefit p{font-weight:700;color:var(--muted);font-size:16px;line-height:1.3;margin-top:4px}
.benefits .btn{position:absolute;left:521px;top:356px;width:158px;text-align:center}

/* certifications */
.certs{position:absolute;top:2046px;left:0;width:1200px;height:295px;background:linear-gradient(180deg,#3a33a3,#2f2a93)}
.certs h2{position:absolute;top:42px;width:100%;text-align:center;color:#fff;font-size:30px}
.badge{position:absolute;top:112px;height:118px;background:rgba(255,255,255,.2);border-bottom:2px solid rgba(255,255,255,.6)}
.badge.box{background:#fff;border:none}

/* contact & social */
.contact{position:absolute;top:2341px;left:0;width:384px;height:404px;background:#fff;padding:58px 0 0 83px}
.contact h2{font-size:31px;margin-bottom:20px}
.contact li{list-style:none;display:flex;gap:14px;align-items:flex-start;font-weight:700;color:var(--muted);font-size:15px;line-height:1.3;margin-bottom:20px}
.contact .social{margin-left:26px}
.contact .social i{background:var(--indigo);width:18px;height:18px}
.feed{position:absolute;top:2341px;left:384px;width:816px;height:404px;background:var(--mist)}
.feed h2{position:absolute;top:58px;width:100%;text-align:center;font-size:31px}
.page-card{position:absolute;left:56px;top:94px;width:330px;height:280px;background:#fff;border:1px solid #ccc}
.page-cover{height:125px;background:linear-gradient(135deg,#0d1a66,#2b64c8);position:relative;color:#fff;font-weight:700;font-size:14px;padding:48px 0 0 86px}
.page-cover .thumb{position:absolute;left:12px;top:30px;width:62px;height:62px;background:#3356b0;border:2px solid #fff}
.page-cover .act{position:absolute;bottom:8px;height:22px;background:#eee;color:#333;font-size:11px;padding:4px 8px;border:1px solid #aaa}
.page-card .friends{padding:10px;font-size:11px;color:#555}
.faces{display:flex;gap:4px;margin-top:6px}
.faces i{width:24px;height:24px;background:#9aa3b5;display:block}
.post{margin:10px;display:flex;gap:8px;font-size:12px;color:var(--indigo);font-weight:700}
.post i{width:40px;height:40px;background:#2f4da3;display:block}
.tweets{position:absolute;left:414px;top:94px;width:330px;height:280px;background:#fff;border:1px solid #ccc;font-size:12px}
.tweets header{display:flex;justify-content:space-between;align-items:center;padding:10px;border-bottom:1px solid #ddd;font-weight:700}
.tweets header span{background:#e4e8ee;border:1px solid #bbb;border-radius:3px;padding:4px 10px;font-size:12px}
.tweet{display:flex;gap:10px;padding:12px 10px 2px}
.tweet i{flex:0 0 36px;height:36px;background:#2f4da3}
.tweet small{display:block;font-size:10px;color:#555;margin-bottom:2px}
.tweet p{font-weight:700;color:#333;line-height:1.2}
.tweets footer{position:absolute;bottom:0;left:0;right:0;background:#eee;padding:8px 10px;color:#555}

.footer{position:absolute;top:2745px;left:0;width:1200px;height:46px;background:var(--indigo);color:#fff;font-size:12px;text-align:center;line-height:46px;text-transform:uppercase}
</style>
</head>
<body>

<div class="brand"><div class="dot"></div><div class="name">Brightmoor Systems<br>Collective</div></div>

<div class="topbar">
  <span><svg width="16" height="16" viewBox="0 0 16 16"><circle cx="8" cy="8" r="7" fill="none" stroke="#fff" stroke-width="1.4"/><path d="M5 4.5l1.5 0 .6 2-1 .8a5 5 0 0 0 2.4 2.4l.8-1 2 .6v1.5c-3.6 0-6.3-2.7-6.3-6.3z" fill="#fff"/></svg>1-800-555-0142</span>
  <span><svg width="16" height="16" viewBox="0 0 16 16"><circle cx="8" cy="8" r="7" fill="none" stroke="#fff" stroke-width="1.4"/><rect x="4" y="5.5" width="8" height="5" fill="none" stroke="#fff"/><path d="M4 5.5l4 3 4-3" fill="none" stroke="#fff"/></svg>HELLO@BRIGHTMOORSYSTEMS.NET</span>
  <span class="social"><i></i><i></i><i></i></span>
</div>

<section class="hero">
  <div class="hero-photo" role="img" aria-label="Consultant touching glowing blue outlined gears on a dark background"></div>
  <nav class="nav"><a class="active">Home</a><a>About Us</a><a>Services</a><a>Benefits of Our Offerings</a><a>News</a><a>Contact</a></nav>
  <div class="hero-band">Brightmoor Systems Collective is a technology consulting company that primarily offers end to end technology advisory services to small businesses lacking their own IT staff. We offer top notch white glove and our customer service and satisfaction is exceed by no one.</div>
</section>

<div class="divider" style="top:802px"></div>

<section class="about">
  <h2 class="heading">About Us</h2>
  <div class="copy">
    <p>Lorem ipsum dolor sit amet, consectetuer adipiscing elit, sed diam nonummy nibh euismod tincidunt ut laoreet dolore magna aliquam erat volutpat. Ut wisi enim ad minim veniam, quis nostrud exerci tation ullamcorper suscipit lobortis nisl ut aliquip ex ea commodo consequat.</p>
    <p>Duis autem vel eum iriure dolor in hendrerit in vulputate velit esse molestie consequat, vel illum dolore eu feugiat nulla facilisis at vero eros et accumsan et iusto odio dignissim qui blandit praesent luptatum zzril delenit augue duis dolore te feugait nulla facilisi.</p>
  </div>
  <a class="btn">Discover More</a>
  <div class="video" role="img" aria-label="Video still of hands holding a tablet with floating app icons"><div class="play"></div></div>
</section>

<div class="divider" style="top:1180px"></div>

<section class="services">
  <h2 class="heading" style="color:#fff">Services</h2>
  <div class="service" style="left:80px;top:116px"><div class="tile"><svg width="50" height="44" viewBox="0 0 50 44" fill="none" stroke="#fff" stroke-width="2.5"><rect x="8" y="4" width="34" height="24"/><path d="M2 36h46l-4-8H6z"/></svg></div><div><h3>Strategic IT Planning</h3><p>Lorem ipsum dolor sit amet, consec tetuer adipiscing elit, sed diam no nummy nibh euismod tincidunt ut laoreet dolore magna.</p></div></div>
  <div class="service" style="left:437px;top:116px"><div class="tile"><svg width="54" height="46" viewBox="0 0 54 46" fill="#fff"><rect x="4" y="30" width="6" height="14"/><rect x="14" y="24" width="6" height="20"/><rect x="24" y="26" width="6" height="18"/><rect x="34" y="18" width="6" height="26"/><rect x="44" y="10" width="6" height="34"/><path d="M4 22l12-10 10 6 20-16" fill="none" stroke="#fff" stroke-width="2.5"/></svg></div><div><h3>Business Continuity Planning</h3><p>Lorem ipsum dolor sit amet, consec tetuer adipiscing elit, sed diam no nummy nibh euismod.</p></div></div>
  <div class="service" style="left:794px;top:116px"><div class="tile"><svg width="58" height="40" viewBox="0 0 58 40" fill="none" stroke="#fff" stroke-width="2.5"><path d="M14 36a10 10 0 0 1 0-20 14 14 0 0 1 27-4 11 11 0 0 1 3 24z"/></svg></div><div><h3>Cloud Computing \ Data Center Solutions</h3><p>Lorem ipsum dolor sit amet, consec tetuer adipiscing elit, sed diam no nummy nibh euismod.</p></div></div>
  <div class="service" style="left:80px;top:252px"><div class="tile"><svg width="50" height="50" viewBox="0 0 50 50" fill="#fff"><rect x="4" y="4" width="42" height="11" rx="2"/><rect x="4" y="19" width="42" height="11" rx="2"/><rect x="4" y="34" width="42" height="11" rx="2"/></svg></div><div><h3>Server Infrastructure</h3><p>Lorem ipsum dolor sit amet, consec tetuer adipiscing elit, sed diam no nummy nibh euismod tincidunt ut laoreet dolore magna.</p></div></div>
  <div class="service" style="left:437px;top:252px"><div class="tile"><svg width="50" height="54" viewBox="0 0 50 54" fill="none" stroke="#fff" stroke-width="2.5"><circle cx="20" cy="18" r="7"/><circle cx="20" cy="18" r="14"/><path d="M20 18v20l-5-4-3 3 10 12h18l4-14-16-5"/></svg></div><div><h3>Virtualization Technologies</h3><p>Lorem ipsum dolor sit amet, consec tetuer adipiscing elit, sed diam no nummy nibh euismod tincidunt ut laoreet dolore magna.</p></div></div>
  <div class="service" style="left:794px;top:252px"><div class="tile"><svg width="54" height="44" viewBox="0 0 54 44" fill="#fff"><rect x="19" y="2" width="16" height="11"/><rect x="2" y="31" width="14" height="11"/><rect x="20" y="31" width="14" height="11"/><rect x="38" y="31" width="14" height="11"/><path d="M27 13v9M9 31v-9h36v9M27 22v9" fill="none" stroke="#fff" stroke-width="2.5"/></svg></div><div><h3>Project Management</h3><p>Lorem ipsum dolor sit amet, consec tetuer adipiscing elit, sed diam no nummy nibh euismod tincidunt ut laoreet dolore magna.</p></div></div>
</section>

<div class="divider" style="top:1582px"></div>

<section class="benefits">
  <h2 class="heading">Benefits of Our Offerings</h2>
  <div class="benefit" style="left:126px"><div class="frame"><svg width="76" height="76" viewBox="0 0 76 76"><circle cx="36" cy="40" r="32" fill="var(--indigo)"/><circle cx="36" cy="40" r="23" fill="#fff"/><circle cx="36" cy="40" r="15" fill="var(--indigo)"/><circle cx="36" cy="40" r="7" fill="#fff"/><path d="M36 40L68 8" stroke="var(--indigo)" stroke-width="4"/><path d="M60 4l10 2 2 10-8-2z" fill="var(--indigo)"/></svg></div><h3>VERY DEDICATED</h3><p>We are small firm but are<br>very dedicated.</p></div>
  <div class="benefit" style="left:444px"><div class="frame"><svg width="60" height="84" viewBox="0 0 60 84"><path d="M14 46l-8 34 12-6 6 10 6-30zM46 46l8 34-12-6-6 10-6-30z" fill="var(--indigo)"/><circle cx="30" cy="28" r="26" fill="var(--indigo)"/><circle cx="30" cy="28" r="18" fill="#fff"/><path d="M30 16l3.5 8 8.5.5-6.5 5.5 2 8.5-7.5-4.5-7.5 4.5 2-8.5-6.5-5.5 8.5-.5z" fill="var(--indigo)"/></svg></div><h3>CERTIFIED ADVISORS</h3><p>We hold many certifications<br>from Quillora &amp; Tessfold.</p></div>
  <div class="benefit" style="left:761px"><div class="frame"><svg width="76" height="76" viewBox="0 0 76 76"><rect x="26" y="4" width="30" height="44" rx="4" fill="none" stroke="var(--indigo)" stroke-width="4"/><path d="M36 30l5-8 5 8M41 22v14" fill="none" stroke="var(--indigo)" stroke-width="3"/><path d="M4 52l16-10 20 4h10a4 4 0 0 1 0 8H34M20 70l10-8 20 2 20-16" fill="none" stroke="var(--indigo)" stroke-width="5" stroke-linejoin="round"/></svg></div><h3>CUSTOMER SERVICE</h3><p>Our customer service and<br>satisfaction is exceed by no one.</p></div>
  <a class="btn">Learn More</a>
</section>

<div class="divider" style="top:2016px"></div>

<section class="certs">
  <h2 class="heading" style="color:#fff">Certifications</h2>
  <div class="badge" style="left:290px;width:168px" role="img" aria-label="Quillora solutions expert certification badge"></div>
  <div class="badge" style="left:528px;width:170px" role="img" aria-label="Quillora solutions expert certification badge"></div>
  <div class="badge box" style="left:774px;width:134px" role="img" aria-label="Tessfold certified professional badge"></div>
</section>

<div class="divider" style="top:2311px"></div>

<section class="contact">
  <h2 class="heading">Contact</h2>
  <ul>
    <li><svg width="14" height="18" viewBox="0 0 14 18"><path d="M7 0a7 7 0 0 1 7 7c0 5-7 11-7 11S0 12 0 7a7 7 0 0 1 7-7z" fill="#555"/><circle cx="7" cy="7" r="2.6" fill="#fff"/></svg><span>48 Harlow Lane<br>New York City, NY 10014</span></li>
    <li><svg width="16" height="14" viewBox="0 0 16 14"><path d="M1 4c0-3 14-3 14 0v2h-4V4H5v2H1zM3 7h10l2 7H1z" fill="#555"/></svg><span>1800.555.0142</span></li>
    <li><svg width="16" height="12" viewBox="0 0 16 12"><rect x="0.5" y="0.5" width="15" height="11" fill="none" stroke="#555"/><path d="M.5 .5l7.5 6 7.5-6" fill="none" stroke="#555"/></svg><span>hello@brightmoorsystems.net</span></li>
  </ul>
  <div class="social"><i></i><i></i><i></i></div>
</section>

<section class="feed">
  <h2 class="heading">Latest From Social Media</h2>
  <div class="page-card">
    <div class="page-cover"><div class="thumb"></div>Brightmoor Systems Collective<span class="act" style="left:10px">Like Page</span><span class="act" style="right:10px">Book Now</span></div>
    <div class="friends">Be the first of your friends to like this<div class="faces"><i></i><i></i><i></i><i></i><i></i><i></i><i></i><i></i></div></div>
    <div class="post"><i></i><span>Brightmoor Systems Collective<br><small style="color:#888;font-weight:400">8 hrs</small></span></div>
  </div>
  <div class="tweets">
    <header>TWEETS<span>Follow @BrightmoorSys</span></header>
    <div class="tweet"><i></i><div><small>Sept 29, 2015</small><p>Lorem ipsum dolor sit amet, consectetuer adip iscing elit, sed diam nonummy nibh euismod</p></div></div>
    <div class="tweet"><i></i><div><small>Sept 25, 2015</small><p>Lorem ipsum dolor sit amet, consectetuer adi piscing elit, sed diam nonummy nibh euismod tincidunt ut laoreet dolore magna aliquam erat volutpat. Ut wisi enim ad minim veniam.</p></div></div>
    <footer>Tweet to @BrightmoorSys</footer>
  </div>
</section>

<footer class="footer">Copyright © 2015 Brightmoor Systems Collective. All rights reserved.</footer>

</body>
</html>
```